Social media app sign-up flow that asks users to give personal info and connect with other apps

Design an interactive, fun, and playful sign-up flow in which you are providing information about you, your interests, and connecting with different API plug-ins such as Fendora, WorkLoop, Tunevo, etc. (using the brand palette attached).

Basic wireframe, and business requirements are also attached.

Target Market(s)

Gen Z + Millennials (ages 22-40)

Font styles to use
Sans Serif

Colors
fbed22
fbee3d
fbf289

Requirements
Must have
• Forms for users to submit their info. Follow the color palette attached.

Connect with Fendora, Connect with WorkLoop, Connect with Tunevo, Connect with Gatherwick buttons
Nice to have
• I like the way you can use cards to submit your information for each category. Interactive card design for providing your info
Should not have
• Basic outdated designs, long forms

```html
<!DOCTYPE html>
<html lang="en">
<head>
<meta charset="utf-8">
<title>UI Design screen</title>
<link href="https://fonts.googleapis.com/css2?family=Figtree:wght@300;400;500;600;700;800&display=swap" rel="stylesheet">
<style>
:root{
  --bg:#1a1a1a;
  --yellow:#ffc430;
  --ink:#1d1d1d;
  --text:#333;
  --muted:#8a8a8a;
  --field:#f3f4f5;
  --field-line:#dcdcdc;
  --tile:#f4f4f4;
  --fendora:#4a6ea8;
  --workloop:#0e73b1;
  --tunevo:#2fd35b;
  --mailora:#e04a3a;
  --orchardly:#111;
  --number:#272b2f;
}
*{margin:0;padding:0;box-sizing:border-box}
html,body{width:1200px;height:2683px;overflow:hidden;background:var(--bg)}
body{font-family:"Figtree",sans-serif;color:var(--text)}
.board{position:absolute;left:0;top:0;width:1152px;height:2576px;transform:scale(1.041667);transform-origin:0 0}
.section-number{position:absolute;left:494px;top:52px;font-size:150px;font-weight:800;color:var(--number);line-height:1;letter-spacing:-4px}
.section-title{position:absolute;left:468px;top:118px;font-size:58px;font-weight:700;color:var(--yellow);line-height:1;letter-spacing:-.5px}

.screen{position:absolute;background:#fff;overflow:hidden}
.screen .fill{position:absolute;left:0;top:var(--h);width:var(--r);height:var(--r);background:var(--yellow)}
.screen .body{position:absolute;left:0;right:0;top:var(--h);bottom:0;background:#fff;border-top-left-radius:var(--r)}
.screen .hdr{position:absolute;left:0;top:0;width:100%;height:var(--h);background:var(--yellow);border-bottom-right-radius:var(--r)}
.screen > *{position:absolute}
.back{left:20px;top:14px;width:14px;height:18px}
.kicker{color:#fff;font-weight:300;line-height:1}
.headline{color:#fff;font-weight:700;line-height:1;letter-spacing:.3px}
.center{left:0;width:100%;text-align:center}
.note{font-size:13px;color:var(--text)}
.sub{font-size:14px;color:var(--text);line-height:19px}

.tile{width:90px;height:90px;background:var(--tile);border-radius:12px;display:flex;flex-direction:column;align-items:center;padding-top:8px}
.tile svg{width:62px;height:58px}
.tile span{margin-top:2px;font-size:14px;font-weight:700;letter-spacing:2px;color:var(--yellow)}

.field{height:36px;background:var(--field);border:1px solid var(--field-line);font-size:12px;color:#555;display:flex;align-items:center;padding-left:18px}
.field .pen{position:absolute;right:10px;top:50%;margin-top:-8px;width:16px;height:16px}
.btn{width:236px;height:33px;display:flex;align-items:center;color:#fff;font-size:12px;font-weight:500}
.btn .mark{width:33px;height:100%;background:rgba(0,0,0,.14);flex:none}
.btn span{padding-left:24px}
.btn.fendora{background:var(--fendora)}
.btn.workloop{background:var(--workloop)}
.btn.tunevo{background:var(--tunevo)}
.btn.mailora{background:var(--mailora)}
.btn.orchardly{background:var(--orchardly)}
.primary{background:var(--yellow);color:#fff;font-size:12px;display:flex;align-items:center;justify-content:center}
.or{left:36px;width:237px;height:14px;font-size:11px;color:#444;text-align:center}
.or:before,.or:after{content:"";position:absolute;top:7px;width:100px;height:1px;background:#999}
.or:before{left:0}.or:after{right:0}
.add{font-size:13px;font-weight:700;color:var(--yellow)}
.photo{width:83px;height:83px;border-radius:10px}
.thumb{width:52px;height:52px}
.link{color:var(--yellow)}
</style>
</head>
<body>
<main class="board">
  <div class="section-number">07</div>
  <h1 class="section-title">UI Design screen</h1>

  <!-- About you -->
  <section class="screen" style="left:83px;top:56px;width:343px;height:742px;--h:151px;--r:60px">
    <div class="fill"></div><div class="body"></div><div class="hdr"></div>
    <div class="kicker" style="left:40px;top:50px;font-size:24px">Tell me</div>
    <div class="headline" style="left:40px;top:84px;font-size:38px">ABOUT YOU</div>
    <p class="sub center" style="top:186px">You can start where you are and change<br>everything you want</p>

    <div class="tile" style="left:48px;top:280px">
      <svg viewBox="0 0 62 58"><path d="M10 28 31 8l21 20" fill="none" stroke="#111" stroke-width="3" stroke-linejoin="round"/><path d="M15 25v26h32V25L31 10z" fill="var(--yellow)" stroke="#111" stroke-width="3" stroke-linejoin="round"/><path d="M26 51V37h10v14" fill="#fff" stroke="#111" stroke-width="3"/></svg>
      <span>PLACES</span>
    </div>
    <div class="tile" style="left:205px;top:280px">
      <svg viewBox="0 0 62 58"><path d="M19 27v12c0 4 24 4 24 0V27" fill="var(--yellow)" stroke="#111" stroke-width="3"/><path d="M6 22 31 11l25 11-25 11z" fill="var(--yellow)" stroke="#111" stroke-width="3" stroke-linejoin="round"/><path d="M52 24v12" stroke="#111" stroke-width="3"/></svg>
      <span>SCHOOLS</span>
    </div>
    <div class="tile" style="left:48px;top:386px">
      <svg viewBox="0 0 62 58"><rect x="10" y="16" width="42" height="32" rx="2" fill="var(--yellow)" stroke="#111" stroke-width="3"/><path d="M24 16v-6h14v6" fill="none" stroke="#111" stroke-width="3"/><path d="M20 16v32M42 16v32" stroke="#111" stroke-width="3"/></svg>
      <span>WORK</span>
    </div>
    <div class="tile" style="left:205px;top:386px">
      <svg viewBox="0 0 62 58"><circle cx="36" cy="18" r="9" fill="#fff" stroke="#111" stroke-width="3"/><circle cx="27" cy="20" r="10" fill="var(--yellow)" stroke="#111" stroke-width="3"/><path d="M9 48c0-11 8-16 18-16s18 5 18 16z" fill="var(--yellow)" stroke="#111" stroke-width="3" stroke-linejoin="round"/></svg>
      <span>PEOPLE</span>
    </div>
    <div class="tile" style="left:48px;top:493px">
      <svg viewBox="0 0 62 58"><rect x="9" y="11" width="44" height="38" rx="2" fill="var(--yellow)" stroke="#111" stroke-width="3"/><path d="M9 20h44M18 6v9M31 6v9M44 6v9M16 28h30M16 35h30M16 42h30" stroke="#111" stroke-width="3"/></svg>
      <span>EVENTS</span>
    </div>
    <div class="tile" style="left:205px;top:493px">
      <svg viewBox="0 0 62 58"><rect x="9" y="11" width="44" height="38" rx="2" fill="var(--yellow)" stroke="#111" stroke-width="3"/><path d="M9 20h44M18 6v9M31 6v9M44 6v9" stroke="#111" stroke-width="3"/><path d="M24 33l6 6 9-10" fill="none" stroke="#111" stroke-width="3"/></svg>
      <span>EVENTS</span>
    </div>
    <div class="tile" style="left:48px;top:600px">
      <svg viewBox="0 0 62 58"><path d="M26 40V12l20-4v26" fill="none" stroke="#111" stroke-width="3"/><ellipse cx="20" cy="41" rx="7" ry="6" fill="var(--yellow)" stroke="#111" stroke-width="3"/><ellipse cx="40" cy="35" rx="7" ry="6" fill="var(--yellow)" stroke="#111" stroke-width="3"/></svg>
      <span>MUSIC</span>
    </div>
    <div class="tile" style="left:205px;top:600px">
      <svg viewBox="0 0 62 58"><circle cx="31" cy="12" r="6" fill="var(--yellow)" stroke="#111" stroke-width="3"/><circle cx="19" cy="28" r="6" fill="var(--yellow)" stroke="#111" stroke-width="3"/><circle cx="43" cy="28" r="6" fill="var(--yellow)" stroke="#111" stroke-width="3"/><path d="M8 50c0-8 5-12 11-12s11 4 11 12zM32 50c0-8 5-12 11-12s11 4 11 12z" fill="var(--yellow)" stroke="#111" stroke-width="3" stroke-linejoin="round"/><path d="M22 22c1-4 4-6 9-6s8 2 9 6" fill="none" stroke="#111" stroke-width="3"/></svg>
      <span>TEAM</span>
    </div>
  </section>

  <!-- Phone sign up -->
  <section class="screen" style="left:469px;top:224px;width:310px;height:671px;--h:137px;--r:50px">
    <div class="fill"></div><div class="body"></div><div class="hdr"></div>
    <div class="headline" style="left:36px;top:34px;font-size:23px;line-height:29px;letter-spacing:0">Enjoy events nearby<br>and meet new<br>friends</div>
    <div class="center" style="top:161px;font-size:17px;font-weight:700;color:var(--ink)">What’s your number?</div>
    <div class="center note" style="top:189px">We’ll text code to verify this number</div>
    <div class="field" style="left:36px;top:221px;width:52px;height:36px;padding-left:6px">
      <svg width="40" height="16" viewBox="0 0 40 16"><rect x="0" y="1" width="24" height="15" fill="#2c4f9e"/><rect x="0" y="7" width="24" height="3" fill="#fff"/><rect x="10" y="1" width="4" height="15" fill="#fff"/><rect x="0" y="8" width="24" height="1" fill="#d22"/><rect x="11" y="1" width="2" height="15" fill="#d22"/><path d="M29 7h8l-4 4z" fill="#777"/></svg>
    </div>
    <div class="field" style="left:96px;top:221px;width:176px;color:#aaa">01-2345-678-0</div>
    <div class="primary" style="left:36px;top:271px;width:236px;height:36px">Continue</div>
    <div class="or" style="top:333px">or</div>
    <div class="btn mailora" style="left:36px;top:360px"><i class="mark"></i><span>Continue with Mailora</span></div>
    <div class="btn fendora" style="left:36px;top:404px"><i class="mark"></i><span>Continue with Fendora</span></div>
    <div class="btn orchardly" style="left:36px;top:448px"><i class="mark" style="background:#000"></i><span>Continue with Orchardly</span></div>
    <div class="btn workloop" style="left:36px;top:493px"><i class="mark"></i><span>Continue with WorkLoop</span></div>
    <p class="center" style="top:555px;font-size:10px;line-height:17px;color:#444">By signing up you accept the <span class="link">Terms of Service</span> and<br><span class="link">Privacy Policy</span></p>
    <div class="center" style="top:610px;font-size:12px;color:#444">Already have an account? <span class="link">Log in</span></div>
  </section>

  <!-- Music -->
  <section class="screen" style="left:807px;top:224px;width:310px;height:671px;--h:137px;--r:50px">
    <div class="fill"></div><div class="body"></div><div class="hdr"></div>
    <svg class="back" viewBox="0 0 14 18"><path d="M10 3 4 9l6 6" fill="none" stroke="#fff" stroke-width="1.6"/></svg>
    <div class="headline" style="left:36px;top:48px;font-size:36px">MUSIC</div>
    <div class="kicker" style="left:36px;top:89px;font-size:24px">You love</div>
    <div class="center note" style="top:178px">Fill out manually</div>
    <div class="thumb" role="img" aria-label="Portrait of the artist Brielle Sparks" style="left:36px;top:208px;background:linear-gradient(160deg,#c9c9c9,#6f6f6f)"></div>
    <div class="field" style="left:96px;top:208px;width:176px;height:52px;padding-left:7px">Brielle Sparks<svg class="pen" viewBox="0 0 16 16"><path d="M2 14l1-4 8-8 3 3-8 8z" fill="var(--yellow)"/></svg></div>
    <div class="thumb" role="img" aria-label="Group photo of the band The Beetroots" style="left:36px;top:276px;background:linear-gradient(160deg,#9a9a9a,#2a2a2a)"></div>
    <div class="field" style="left:96px;top:276px;width:176px;height:52px;padding-left:7px">The Beetroots<svg class="pen" viewBox="0 0 16 16"><path d="M2 14l1-4 8-8 3 3-8 8z" fill="var(--yellow)"/></svg></div>
    <div class="center add" style="top:348px">+ Add More Here</div>
    <div class="or" style="top:418px">or</div>
    <p class="center note" style="top:449px;line-height:17px">Fill out automatically with your social<br>media profile</p>
    <div class="btn fendora" style="left:36px;top:499px"><i class="mark"></i><span>Connect with Fendora</span></div>
    <div class="btn tunevo" style="left:36px;top:556px"><i class="mark"></i><span>Connect with Tunevo</span></div>
  </section>

  <!-- People -->
  <section class="screen" style="left:83px;top:833px;width:343px;height:742px;--h:151px;--r:60px">
    <div class="fill"></div><div class="body"></div><div class="hdr"></div>
    <svg class="back" viewBox="0 0 14 18"><path d="M10 3 4 9l6 6" fill="none" stroke="#fff" stroke-width="1.6"/></svg>
    <div class="headline" style="left:40px;top:53px;font-size:38px">PEOPLE</div>
    <div class="kicker" style="left:40px;top:99px;font-size:24px">You know</div>
    <p class="center sub" style="top:188px">Fill out automatically with your social<br>media profile</p>
    <div class="btn fendora" style="left:40px;top:259px;width:262px;height:37px"><i class="mark" style="width:37px"></i><span style="padding-left:31px">Sync with Fendora</span></div>
    <div style="left:18px;top:339px;width:307px;height:1px;background:#999"></div>
    <div class="photo" role="img" aria-label="Profile photo of a friend" style="left:18px;top:370px;background:linear-gradient(150deg,#8a3a34,#2a1a1a)"></div>
    <div class="photo" role="img" aria-label="Profile photo of a friend" style="left:130px;top:370px;background:linear-gradient(150deg,#6c6c6c,#2e2e2e)"></div>
    <div class="photo" role="img" aria-label="Profile photo of a friend" style="left:242px;top:370px;background:linear-gradient(150deg,#a07a52,#3b2a1c)"></div>
    <div class="photo" role="img" aria-label="Profile photo of a friend" style="left:18px;top:477px;background:linear-gradient(150deg,#d0c4b8,#2c3550)"></div>
    <div class="photo" role="img" aria-label="Profile photo of a friend" style="left:130px;top:477px;background:linear-gradient(150deg,#f2ece4,#d8b89c)"></div>
    <div class="photo" role="img" aria-label="Profile photo of a friend" style="left:242px;top:477px;background:linear-gradient(150deg,#4b7f86,#1d3438)"></div>
    <div class="photo" role="img" aria-label="Profile photo of a friend" style="left:18px;top:583px;background:linear-gradient(150deg,#c9b8a0,#6f5a44)"></div>
    <div class="photo" role="img" aria-label="Profile photo of a friend" style="left:130px;top:583px;background:linear-gradient(150deg,#f4f4f4,#2aa66a)"></div>
    <div class="photo" role="img" aria-label="Profile photo of a friend" style="left:242px;top:583px;background:linear-gradient(150deg,#5a3a2a,#d57a2e)"></div>
    <div class="photo" role="img" aria-label="Profile photo of a friend" style="left:18px;top:690px;background:linear-gradient(150deg,#5f6f5a,#1e1e1e)"></div>
    <div class="photo" role="img" aria-label="Profile photo of a friend" style="left:130px;top:690px;background:linear-gradient(150deg,#6f7a4a,#a0603a)"></div>
    <div class="photo" role="img" aria-label="Profile photo of a friend" style="left:242px;top:690px;background:linear-gradient(150deg,#7a1a2a,#3a0a12)"></div>
  </section>

  <!-- Place -->
  <section class="screen" style="left:469px;top:930px;width:311px;height:674px;--h:137px;--r:50px">
    <div class="fill"></div><div class="body"></div><div class="hdr"></div>
    <svg class="back" viewBox="0 0 14 18"><path d="M10 3 4 9l6 6" fill="none" stroke="#fff" stroke-width="1.6"/></svg>
    <div class="headline" style="left:37px;top:49px;font-size:36px">PLACE</div>
    <div class="kicker" style="left:37px;top:89px;font-size:24px">You’ve lived</div>
    <div class="center note" style="top:179px">Fill out manually</div>
    <div class="field" style="left:37px;top:209px;width:237px">Chicago<svg class="pen" viewBox="0 0 16 16"><path d="M2 14l1-4 8-8 3 3-8 8z" fill="var(--yellow)"/></svg></div>
    <div class="field" style="left:37px;top:260px;width:237px">Madrid<svg class="pen" viewBox="0 0 16 16"><path d="M2 14l1-4 8-8 3 3-8 8z" fill="var(--yellow)"/></svg></div>
    <div class="field" style="left:37px;top:311px;width:237px">London<svg class="pen" viewBox="0 0 16 16"><path d="M2 14l1-4 8-8 3 3-8 8z" fill="var(--yellow)"/></svg></div>
    <div class="center add" style="top:367px">+ Add More Here</div>
    <div class="or" style="left:37px;top:419px">or</div>
    <p class="center note" style="top:450px;line-height:17px">Fill out automatically with your social<br>media profile</p>
    <div class="btn fendora" style="left:37px;top:501px;width:237px"><i class="mark"></i><span>Connect with Fendora</span></div>
    <div class="btn workloop" style="left:37px;top:558px;width:237px"><i class="mark"></i><span>Connect with WorkLoop</span></div>
  </section>

  <!-- School -->
  <section class="screen" style="left:807px;top:930px;width:311px;height:675px;--h:137px;--r:50px">
    <div class="fill"></div><div class="body"></div><div class="hdr"></div>
    <svg class="back" viewBox="0 0 14 18"><path d="M10 3 4 9l6 6" fill="none" stroke="#fff" stroke-width="1.6"/></svg>
    <div class="headline" style="left:37px;top:49px;font-size:36px">SCHOOL</div>
    <div class="kicker" style="left:37px;top:89px;font-size:24px">You’ve attended</div>
    <div class="center note" style="top:179px">Fill out manually</div>
    <div class="field" style="left:37px;top:209px;width:237px;height:69px;display:block;padding:11px 0 0 13px;line-height:15px;font-size:11.5px">
      <b style="color:#222;font-weight:700">Stanmore University</b><br>Bachelor’s degree, Information Technology<br><span style="font-size:10px;color:#777">2015-2019</span>
    </div>
    <div class="center add" style="top:294px">+ Add More Here</div>
    <div class="or" style="left:37px;top:420px">or</div>
    <p class="center note" style="top:451px;line-height:17px">Fill out automatically with your social<br>media profile</p>
    <div class="btn workloop" style="left:37px;top:502px;width:237px"><i class="mark"></i><span>Connect with WorkLoop</span></div>
  </section>

  <!-- Sport team -->
  <section class="screen" style="left:83px;top:1666px;width:343px;height:741px;--h:152px;--r:60px">
    <div class="fill"></div><div class="body"></div><div class="hdr"></div>
    <svg class="back" viewBox="0 0 14 18"><path d="M10 3 4 9l6 6" fill="none" stroke="#fff" stroke-width="1.6"/></svg>
    <div class="kicker" style="left:34px;top:48px;font-size:26px">Your favourite</div>
    <div class="headline" style="left:34px;top:83px;font-size:38px">SPORT TEAM</div>
    <div class="center sub" style="top:195px">Fill out manually</div>
    <div class="field" style="left:41px;top:245px;width:57px;height:39px;padding-left:6px">
      <svg width="46" height="26" viewBox="0 0 46 26"><circle cx="13" cy="13" r="11" fill="var(--yellow)"/><path d="M2 13h22M13 2v22M5 5c4 4 4 12 0 16M21 5c-4 4-4 12 0 16" stroke="#fff" stroke-width="1.5" fill="none"/><path d="M33 11h8l-4 4z" fill="#777"/></svg>
    </div>
    <div class="field" style="left:107px;top:245px;width:195px;height:39px;padding-left:15px;font-size:13px;color:#222">Choose league
      <svg style="position:absolute;right:10px;top:15px" width="12" height="8" viewBox="0 0 12 8"><path d="M0 1h12L6 7z" fill="#777"/></svg>
    </div>
    <div class="field" style="left:41px;top:297px;width:261px;height:39px;padding-left:20px;font-size:13px">Location</div>
    <div class="field" style="left:41px;top:351px;width:261px;height:39px;padding-left:20px;font-size:13px">Official team name here...</div>
    <div class="primary" style="left:40px;top:651px;width:260px;height:39px;font-size:13px">Save</div>
  </section>
</main>
</body>
</html>
```